Senior Care Industry E-Blast Design

We are looking for a fresh e-blast design that is in line with company branding (qmsreit.com) but also has a fun, fresh, creative design flare to it! Please use the attached logo and include the copy below. The image attached can be purchased for use, or used as a reference to look / feel - we are open to other fun, creative visuals!
Specs:
600px w x 1500px h
Copy:
(bold, big) We invest in your vision, so you can focus on delivering exceptional care.
(body copy) With our capital behind you, we work together to deliver results that matter—for your business and your residents. Whether it’s navigating today’s challenges or planning for tomorrow’s opportunities, we’re focused on what matters most—your success. (bold / colored)
Our custom financing solutions include:
Acquisitions
Construction
Refinancing
Recapitalizations
Structured Leases
Bridge
Mezzanine
Unitranche
NNN Lease
Preferred Equity
(bold / big) QMS: Financing Freedom, Empowering Care
Headed to OVIN? See you there!

```html
<!DOCTYPE html>
<html lang="en">
<head>
<meta charset="utf-8">
<title>QMS REIT – Financing Freedom, Empowering Care</title>
<link rel="stylesheet" href="https://fonts.googleapis.com/css2?family=Montserrat:wght@400;500;600;700;800;900&display=swap">
<style>
  :root{
    --navy:#0b1f5c;
    --navy-deep:#071a52;
    --royal:#0a5bc4;
    --icon-blue:#0a63d0;
    --sky:#5bc3ec;
    --pill:#6aaeea;
    --ice:#d6effb;
    --bubble:#ececec;
    --ink:#2b2b2b;
    --heading-blue:#0a3a9a;
    --white:#ffffff;
    --stage:#b6b6b6;
    --dots:#1c2f6e;
  }
  *{box-sizing:border-box;margin:0;padding:0}
  html,body{width:1200px;height:2317px;overflow:hidden}
  body{background:var(--stage);font-family:"Montserrat",sans-serif;position:relative}
  .eblast{position:absolute;left:193px;top:142px;width:814px;height:2034px;background:var(--white);overflow:hidden}
  .abs{position:absolute}

  /* Hero */
  .hero{left:0;top:0;width:814px;height:442px;background:linear-gradient(215deg,var(--royal) 0%,#0a3a94 35%,var(--navy-deep) 75%)}
  .hero-art{left:76px;top:96px;width:283px;height:306px;border-radius:6px;background:linear-gradient(160deg,#1570d6,#0b3f9e)}
  .brand{left:401px;top:100px;display:flex;align-items:center;gap:12px;color:var(--white);font-weight:800;font-size:40px;letter-spacing:1px}
  .brand-mark{width:34px;height:34px;border-radius:50%;background:var(--white)}
  .hero-copy{left:396px;top:210px;color:var(--white)}
  .hero-lead{font-size:22px;font-weight:700;line-height:27px}
  .hero-big{font-size:61px;font-weight:800;color:var(--sky);line-height:66px;margin-top:6px;letter-spacing:-.5px}
  .hero-sub{font-size:38px;font-weight:800;color:var(--sky);line-height:40px;letter-spacing:-.3px}

  /* Intro */
  .bubble{left:76px;width:463px;background:var(--bubble);border-radius:60px;box-shadow:0 6px 10px rgba(0,0,0,.15);padding:30px 40px 0 44px;color:var(--ink);font-size:22px;font-weight:500;line-height:27px}
  .bubble-one{top:478px;height:153px}
  .bubble-two{top:650px;height:194px;padding-top:22px}
  .bubble-emph{margin-top:16px;color:var(--heading-blue);font-weight:800;font-size:21px;line-height:27px}
  .intro-art{left:558px;top:533px;width:225px;height:306px;border-radius:6px;background:linear-gradient(180deg,#f3b63a,#d8474f 55%,#3b79b4)}

  /* Solutions */
  .solutions{left:0;top:880px;width:814px;height:360px;background:var(--ice)}
  .solutions-title{left:0;top:30px;width:814px;text-align:center;font-size:29px;font-weight:700;color:var(--heading-blue)}
  .solution{transform:translateX(-50%);text-align:center;width:240px}
  .solution-icon{width:63px;height:63px;border-radius:50%;background:var(--icon-blue);margin:0 auto;display:flex;align-items:center;justify-content:center}
  .solution-label{font-size:24px;font-weight:700;color:var(--ink);margin-top:22px}
  .vdots{width:0;border-left:2px dotted var(--dots)}
  .hdots{height:0;border-top:2px dotted var(--dots)}

  /* Structures */
  .structures-art{left:76px;top:1253px;width:378px;height:247px;border-radius:6px;background:linear-gradient(160deg,#3f7fb3,#e2454f 60%,#f2b53b)}
  .structures{left:504px;top:1296px;list-style:none}
  .structures li{display:flex;align-items:center;gap:12px;font-size:25px;font-weight:600;color:var(--ink);height:39.5px}

  /* Footer */
  .footer{left:0;top:1533px;width:814px;height:501px;background:var(--navy)}
  .tagline{left:75px;top:44px;font-size:40px;line-height:41px;color:var(--white);font-weight:400}
  .tagline strong{display:block;color:var(--sky);font-weight:800}
  .footer-art{left:459px;top:30px;width:284px;height:189px;border-radius:6px;background:linear-gradient(160deg,#a9d3e6,#f2b53b 55%,#d8474f)}
  .event{left:0;top:249px;width:814px;text-align:center;color:var(--white);font-size:50px;line-height:62px;font-weight:900}
  .pill{left:277px;top:313px;width:260px;height:42px;border-radius:21px;background:var(--pill);color:var(--white);font-weight:800;font-size:25px;display:flex;align-items:center;justify-content:center}
  .site{left:0;top:367px;width:814px;text-align:center;color:var(--white);font-size:23px;line-height:28px;font-weight:700;letter-spacing:6px}
  .social{left:376px;top:406px;display:flex;gap:10px}
  .social span{width:20px;height:20px;border-radius:50%;background:var(--pill)}
</style>
</head>
<body>
<main class="eblast">

  <section class="abs hero">
    <svg class="abs" style="left:0;top:0" width="814" height="442" aria-hidden="true">
      <g fill="none" stroke="#3a5aa8" stroke-width="2">
        <path d="M630 40 l8 -8 l8 8 l8 -8 l8 8 l8 -8"/>
        <path d="M777 96 v90" stroke-dasharray="8 8"/>
        <path d="M45 138 v90" stroke-dasharray="8 8"/>
        <rect x="52" y="308" width="30" height="30"/><rect x="58" y="302" width="30" height="30"/>
      </g>
      <path d="M655 128 h12 v-12 h12 v12 h12 v12 h-12 v12 h-12 v-12 h-12z" fill="#4e78c2"/>
      <path d="M0 82 a16 16 0 0 1 30 -4 a12 12 0 0 1 30 6 h-60z" fill="#4e6bb4"/>
    </svg>
    <div class="abs hero-art" role="img" aria-label="Illustration of a caregiver pushing a smiling senior in a wheelchair"></div>
    <div class="abs brand"><span class="brand-mark"></span>QMS</div>
    <div class="abs hero-copy">
      <p class="hero-lead">We invest in your vision,<br>so you can focus on</p>
      <h1 class="hero-big">Delivering</h1>
      <p class="hero-sub">Exceptional Care</p>
    </div>
  </section>

  <div class="abs bubble bubble-one">With our capital behind you, we work together to deliver results that matter—for your business and your residents.</div>
  <div class="abs bubble bubble-two">Whether it’s navigating today’s challenges or planning for tomorrow’s opportunities
    <p class="bubble-emph">WE’RE FOCUSED ON WHAT MATTERS MOST—YOUR SUCCESS</p>
  </div>
  <div class="abs intro-art" role="img" aria-label="Illustration of a carer helping a senior man walk with a frame"></div>

  <section class="abs solutions">
    <h2 class="abs solutions-title">Our custom financing solutions include</h2>
    <div class="abs vdots" style="left:296px;top:84px;height:112px"></div>
    <div class="abs vdots" style="left:522px;top:84px;height:112px"></div>
    <div class="abs hdots" style="left:77px;top:208px;width:319px"></div>
    <div class="abs hdots" style="left:419px;top:208px;width:320px"></div>
    <div class="abs vdots" style="left:407px;top:218px;height:112px"></div>

    <div class="abs solution" style="left:174px;top:84px">
      <div class="solution-icon"><svg width="30" height="30" viewBox="0 0 30 30" fill="#fff"><path d="M3 14 l7 -5 l5 3 l5 -3 l7 5 l-8 8 l-4 -3 l-4 3z"/></svg></div>
      <p class="solution-label">Acquisition</p>
    </div>
    <div class="abs solution" style="left:408px;top:84px">
      <div class="solution-icon"><svg width="30" height="30" viewBox="0 0 30 30" fill="#fff"><rect x="5" y="6" width="8" height="19"/><rect x="15" y="12" width="10" height="13"/></svg></div>
      <p class="solution-label" style="margin-top:18px">Construction</p>
    </div>
    <div class="abs solution" style="left:625px;top:84px">
      <div class="solution-icon"><svg width="34" height="34" viewBox="0 0 34 34"><circle cx="17" cy="17" r="12" fill="none" stroke="#fff" stroke-width="2.5" stroke-dasharray="30 6"/><text x="17" y="23" text-anchor="middle" fill="#fff" font-family="Montserrat,sans-serif" font-weight="800" font-size="16">$</text></svg></div>
      <p class="solution-label" style="margin-top:24px">Refinancing</p>
    </div>
    <div class="abs solution" style="left:245px;top:234px">
      <div class="solution-icon"><svg width="28" height="30" viewBox="0 0 28 30" fill="#fff"><rect x="5" y="4" width="18" height="23" rx="2"/><rect x="9" y="10" width="10" height="2" fill="#0a63d0"/><rect x="9" y="15" width="10" height="2" fill="#0a63d0"/></svg></div>
      <p class="solution-label">Structured Leases</p>
    </div>
    <div class="abs solution" style="left:581px;top:234px">
      <div class="solution-icon"><svg width="30" height="30" viewBox="0 0 30 30" fill="#fff"><circle cx="16" cy="10" r="6"/><path d="M3 22 h8 l6 -3 h7 v3 l-8 4 h-13z"/></svg></div>
      <p class="solution-label">Recapitalizations</p>
    </div>
  </section>

  <div class="abs structures-art" role="img" aria-label="Illustration of a family on a red sofa reviewing plans on a laptop beside large leaves"></div>
  <ul class="abs structures">
    <li><svg width="28" height="28" viewBox="0 0 28 28"><circle cx="14" cy="14" r="13" fill="#0a63d0"/><path d="M8 14 l4 4 l8 -8" stroke="#fff" stroke-width="3" fill="none"/></svg>Bridge</li>
    <li><svg width="28" height="28" viewBox="0 0 28 28"><circle cx="14" cy="14" r="13" fill="#0a63d0"/><path d="M8 14 l4 4 l8 -8" stroke="#fff" stroke-width="3" fill="none"/></svg>Mezzanine</li>
    <li><svg width="28" height="28" viewBox="0 0 28 28"><circle cx="14" cy="14" r="13" fill="#0a63d0"/><path d="M8 14 l4 4 l8 -8" stroke="#fff" stroke-width="3" fill="none"/></svg>Unitranche</li>
    <li><svg width="28" height="28" viewBox="0 0 28 28"><circle cx="14" cy="14" r="13" fill="#0a63d0"/><path d="M8 14 l4 4 l8 -8" stroke="#fff" stroke-width="3" fill="none"/></svg>NNN Lease</li>
    <li><svg width="28" height="28" viewBox="0 0 28 28"><circle cx="14" cy="14" r="13" fill="#0a63d0"/><path d="M8 14 l4 4 l8 -8" stroke="#fff" stroke-width="3" fill="none"/></svg>Preferred Equity</li>
  </ul>

  <section class="abs footer">
    <svg class="abs" style="left:0;top:0" width="814" height="501" aria-hidden="true">
      <g fill="none" stroke="#3a5aa8" stroke-width="2">
        <path d="M358 92 l8 -8 l8 8 l8 -8 l8 8 l8 -8"/>
        <path d="M40 60 v80" stroke-dasharray="8 8"/>
        <rect x="72" y="285" width="30" height="30"/><rect x="78" y="279" width="30" height="30"/>
      </g>
      <path d="M0 460 a16 16 0 0 1 30 -4 a12 12 0 0 1 30 6 h-60z" fill="#4e6bb4"/>
      <line x1="74" y1="236" x2="740" y2="236" stroke="#ffffff" stroke-width="2.5" stroke-dasharray="2 5"/>
    </svg>
    <h2 class="abs tagline">FINANCING<strong>FREEDOM</strong>EMPOWERING<strong>CARE</strong></h2>
    <div class="abs footer-art" role="img" aria-label="Illustration of a senior reading in an armchair while a carer cleans a window"></div>
    <p class="abs event">HEADED TO OVIN?</p>
    <p class="abs pill">SEE YOU THERE!</p>
    <p class="abs site">www.qmsreit.com</p>
    <div class="abs social" aria-hidden="true"><span></span><span></span><span></span></div>
  </section>

</main>
</body>
</html>
```